Industrial Professional Business Card Design (Vantrel Systems)

Would like professional looking business cards. Not too busy leaning towards minimal. Should have a slogan like:
"Industrial Automation and Control".

We are a tech company that programs industrial PLC computers. We also develop custom hardware solutions. Please use the logo for inspiration.

Target Market(s)

Mining, industrial, processing, automation, factory

Industry/Entity Type

Engineering

Contact Information for Business Card

Name, phone, email, website. job title.

Font styles to use
Other font styles liked:
• droid sans

Requirements
Must have
• Use colours that go well with the logo. Not too busy design.

```html
<!DOCTYPE html>
<html lang="en">
<head>
<meta charset="utf-8">
<title>Vantrel Systems – Business Card</title>
<link href="https://fonts.googleapis.com/css2?family=Work+Sans:wght@400;500;600&display=swap" rel="stylesheet">
<style>
  :root {
    --backdrop: #161616;
    --card: #232323;
    --card-edge: #2b2b2b;
    --accent: #f26a21;
    --brand-blue: #2f6aa3;
    --text-light: #ececec;
  }
  * { box-sizing: border-box; margin: 0; padding: 0; }
  html, body { width: 1200px; height: 900px; overflow: hidden; }
  body {
    background: var(--backdrop);
    font-family: "Work Sans", "Noto Sans", sans-serif;
    display: flex;
    flex-direction: column;
    align-items: center;
    justify-content: center;
    gap: 44px;
  }
  .card {
    position: relative;
    width: 630px;
    height: 360px;
    background: linear-gradient(135deg, var(--card) 0%, var(--card-edge) 100%);
    border-bottom: 4px solid var(--accent);
    box-shadow: 0 18px 40px rgba(0,0,0,0.55);
  }
  .brand {
    display: flex;
    align-items: center;
    gap: 12px;
  }
  .brand-dot {
    width: 22px; height: 22px;
    border-radius: 50%;
    background: var(--accent);
    flex: none;
  }
  .brand-name {
    font-weight: 500;
    color: var(--brand-blue);
    white-space: nowrap;
    letter-spacing: 0.01em;
  }

  /* Front */
  .card-front .brand {
    position: absolute;
    left: 0; right: 0; top: 140px;
    justify-content: center;
  }
  .card-front .brand-name { font-size: 40px; }
  .slogan {
    position: absolute;
    left: 0; right: 0; bottom: 22px;
    text-align: center;
    color: var(--text-light);
    font-size: 13.5px;
    font-weight: 500;
    letter-spacing: 0.12em;
    text-transform: uppercase;
  }

  /* Back */
  .card-back .brand {
    position: absolute;
    left: 38px; top: 160px;
  }
  .card-back .brand-name { font-size: 30px; }
  .divider {
    position: absolute;
    left: 334px; top: 70px;
    width: 2px; height: 210px;
    background: var(--accent);
  }
  .contact {
    position: absolute;
    left: 362px; top: 78px;
    color: var(--text-light);
  }
  .person-name {
    color: var(--accent);
    font-size: 22px;
    font-weight: 600;
    letter-spacing: 0.05em;
    text-transform: uppercase;
  }
  .person-role {
    font-size: 15px;
    letter-spacing: 0.06em;
    margin-top: 2px;
  }
  .address {
    font-size: 15px;
    line-height: 1.4;
    letter-spacing: 0.05em;
    margin-top: 18px;
    font-style: normal;
  }
  .channels {
    list-style: none;
    margin-top: 14px;
    font-size: 15px;
    letter-spacing: 0.04em;
  }
  .channels li {
    display: flex;
    align-items: center;
    gap: 8px;
    line-height: 1.55;
  }
  .channels svg {
    width: 12px; height: 12px;
    flex: none;
    stroke: var(--accent);
    fill: none;
    stroke-width: 1.5;
  }
</style>
</head>
<body>
  <section class="card card-front">
    <div class="brand">
      <span class="brand-dot"></span>
      <span class="brand-name">Vantrel Systems</span>
    </div>
    <p class="slogan">Industrial Automation and Control.</p>
  </section>

  <section class="card card-back">
    <div class="brand">
      <span class="brand-dot"></span>
      <span class="brand-name">Vantrel Systems</span>
    </div>
    <div class="divider"></div>
    <div class="contact">
      <h1 class="person-name">Daniel Brecker</h1>
      <p class="person-role">Director</p>
      <address class="address">418 Harlow Street<br>Carden, NE 68102</address>
      <ul class="channels">
        <li>
          <svg viewBox="0 0 12 12" aria-hidden="true"><path d="M3 1 L5 3.5 L4 5 Q5.5 7.5 7 8 L8.5 7 L11 9 L9.5 11 Q3 10 1 2.5 Z"/></svg>
          +330 5127-4036
        </li>
        <li>
          <svg viewBox="0 0 12 12" aria-hidden="true"><rect x="1" y="2.5" width="10" height="7"/><path d="M1 2.5 L6 6.5 L11 2.5"/></svg>
          info@vantrelsystems.com
        </li>
        <li>
          <svg viewBox="0 0 12 12" aria-hidden="true"><circle cx="6" cy="6" r="5"/><ellipse cx="6" cy="6" rx="2.2" ry="5"/><path d="M1 6 H11"/></svg>
          www.vantrelsystems.com
        </li>
      </ul>
    </div>
  </section>
</body>
</html>
```